PowerPoint template design needed for sales and presales presentations

We would like to have a bright and light, contemporary PowerPoint design based on our existing style assets (see attached files).
We are based in Latvia. Our business is ERP systems implementation, IT infrastructure building and supporting our customers. We are moving from traditional Add-hoc projects model to standardized flat-rate offerings. Our technology platform is Dravomell.
The value proposition of our offerings is based around simplicity, transparency, quality, peace of mind, trust, easy of doing business.
I have to add that if any special are being used, they must be unicode to ensure proper Latvian language characters display.
Updates
Hi! The reason is an error at your side. Today it's 24/08/2020 when I started the project and made a payment. Still for some funny reason in the BRIEF I see that the project deadline is set to 20/08/2020. No wonder no designers are applying...
Target Market(s)
Small and medium enterprise
Look and feel
Each slider illustrates characteristics of the customer's brand and the style your logo design should communicate.

```html
<!DOCTYPE html>
<html lang="en">
<head>
<meta charset="utf-8">
<title>Dravomell Presentation Template</title>
<link href="https://fonts.googleapis.com/css2?family=Poppins:wght@400;500;600;700;800&display=swap" rel="stylesheet">
<style>
  :root{
    --page:#e6edf6;
    --white:#ffffff;
    --ink:#111214;
    --grey:#6d7077;
    --soft:#c9ccd1;
    --line:#e3e5e8;
    --yellow:#f3d21b;
    --green:#8cc63f;
    --cyan:#29b6e8;
    --photo-a:#d7dbe0;
    --photo-b:#9aa1aa;
  }
  *{box-sizing:border-box;margin:0;padding:0}
  html,body{width:1200px;height:2700px;overflow:hidden}
  body{background:var(--page);font-family:"Poppins",sans-serif;color:var(--ink);position:relative}
  .slide{position:absolute;width:528px;height:297px;background:var(--white);box-shadow:0 6px 18px rgba(40,60,90,.12);overflow:hidden}
  .col-l{left:60px}.col-r{left:612px}
  .r1{top:300px}.r2{top:652px}.r3{top:1004px}.r4{top:1356px}.r5{top:1708px}.r6{top:2060px}
  .accent{position:absolute;top:0;right:0;display:flex;height:5px;width:150px}
  .accent span{flex:1}
  .accent .a1{background:var(--ink)}.accent .a2{background:var(--yellow)}.accent .a3{background:var(--green)}.accent .a4{background:var(--cyan)}
  .topline{position:absolute;top:0;left:0;right:150px;height:2px;background:var(--ink)}
  .brand{position:absolute;top:16px;right:20px;display:flex;align-items:center;gap:4px;font-size:8px;font-weight:600;color:var(--ink);border:1px solid var(--soft);padding:4px 6px}
  .brand i{width:8px;height:8px;background:var(--ink);display:block}
  .eyebrow{font-size:6px;color:var(--grey);letter-spacing:.5px}
  .title{font-size:18px;font-weight:800;line-height:1.1;text-transform:uppercase}
  .head-block{position:absolute;left:26px;top:22px}
  .head-block .eyebrow{border-left:14px solid var(--ink);padding-left:5px;margin-bottom:3px}
  .copy{font-size:6px;line-height:1.5;color:var(--grey)}
  .h{font-size:8px;font-weight:700}
  .photo{position:absolute;background:linear-gradient(135deg,var(--photo-a),var(--photo-b))}
  .num{width:24px;height:24px;background:var(--ink);color:var(--white);font-size:9px;font-weight:700;display:flex;align-items:center;justify-content:center;flex:none}
  .item{display:flex;gap:8px;align-items:flex-start}
  .dark{background:var(--ink);color:var(--white)}

  /* title */
  .cover .photo{inset:0 0 0 0}
  .cover .label{position:absolute;left:0;top:150px;width:270px;height:64px;background:var(--ink);color:var(--white);display:flex;align-items:center;gap:12px;padding:0 16px}
  .cover .mark{border:1px solid var(--white);font-size:7px;font-weight:600;padding:6px 5px;display:flex;align-items:center;gap:3px}
  .cover .mark i{width:7px;height:7px;background:var(--white);display:block}
  .cover .label p{font-size:13px;font-weight:800;line-height:1.15}

  /* bullets */
  .bullets .grid{position:absolute;left:26px;top:80px;right:26px;display:grid;grid-template-columns:1fr 1fr;gap:26px 30px}

  /* mission */
  .mission .cards{position:absolute;left:26px;right:26px;top:90px;display:flex;gap:12px}
  .mission .card{flex:1;height:150px;border:1px solid var(--soft);padding:14px;display:flex;flex-direction:column;gap:8px}
  .mission .card.dark{border-color:var(--ink)}
  .mission .card.dark .copy{color:#bfc2c7}
  .ico{width:24px;height:24px;border:1px solid currentColor;display:flex;align-items:center;justify-content:center}

  /* service */
  .service .row{position:absolute;left:26px;right:26px;top:80px;display:flex;gap:12px}
  .service .cell{flex:1}
  .service .cell .photo{position:relative;height:96px;margin-bottom:10px}
  .service .sq{width:20px;height:20px;background:var(--ink);margin-bottom:6px}

  /* about */
  .about .photo{left:280px;top:60px;width:230px;height:200px}
  .about .text{position:absolute;left:26px;top:90px;width:230px;display:flex;flex-direction:column;gap:10px}

  /* work */
  .work .stats{position:absolute;left:26px;top:80px;width:220px;display:grid;grid-template-columns:1fr 1fr;gap:10px}
  .work .box{height:80px;display:flex;align-items:center;justify-content:center;font-size:14px;font-weight:800}
  .work .box.light{background:#eef0f2}
  .work .photo{left:266px;top:80px;width:240px;height:170px}

  /* section */
  .section{background:var(--ink)}
  .section .frame{position:absolute;left:164px;top:100px;width:200px;height:97px;border:2px solid var(--white);display:flex;flex-direction:column;align-items:center;justify-content:center;color:var(--white);gap:4px}
  .section .frame .eyebrow{color:#bfc2c7}
  .section .frame p.title{font-size:18px}

  /* process */
  .process .text{position:absolute;left:26px;top:110px;width:200px}
  .process .list{position:absolute;left:280px;top:60px;right:26px;display:flex;flex-direction:column;gap:16px}

  /* laptop */
  .laptop .list{position:absolute;left:26px;top:90px;width:180px;display:flex;flex-direction:column;gap:18px}
  .laptop .photo{left:230px;top:60px;width:280px;height:190px}

  /* chart */
  .chart .bars{position:absolute;left:26px;top:90px;width:260px}
  .chart .side{position:absolute;left:320px;top:80px;right:26px;display:flex;flex-direction:column;gap:10px}
  .chart .side .h{font-size:10px}

  /* testimonial */
  .testi .quotes{position:absolute;left:26px;top:40px;width:250px;display:grid;grid-template-columns:1fr 1fr;gap:10px}
  .testi .q{height:72px;background:var(--ink);color:var(--white);padding:8px;display:flex;gap:6px}
  .testi .q.light{background:#eef0f2;color:var(--ink)}
  .testi .avatar{width:18px;height:18px;border-radius:50%;background:linear-gradient(135deg,#c8a48a,#7a5c4a);flex:none}
  .testi .q .copy{color:inherit;opacity:.75;font-size:5.5px}
  .testi .head{position:absolute;left:310px;top:130px}

  /* thanks */
  .thanks .photo{left:0;top:0;width:528px;height:297px}
  .thanks .panel{position:absolute;right:24px;top:40px;width:210px;height:220px;background:var(--ink);color:var(--white);padding:34px 26px;display:flex;flex-direction:column;gap:24px}
  .thanks .panel p{font-size:17px;font-weight:800;line-height:1.15}
</style>
</head>
<body>

<!-- Title -->
<section class="slide cover col-l r1">
  <div class="photo" role="img" aria-label="Photo of a laptop on a bright office desk"></div>
  <div class="label">
    <div class="mark"><i></i>Dravomell</div>
    <p>YOUR<br>PRESENTATION<br>GOES HERE</p>
  </div>
</section>

<!-- Bullets -->
<section class="slide bullets col-r r1">
  <div class="topline"></div><div class="accent"><span class="a1"></span><span class="a2"></span><span class="a3"></span><span class="a4"></span></div>
  <div class="brand"><i></i>Dravomell</div>
  <div class="head-block"><p class="eyebrow">Simple and clear</p><p class="title">Bullet Points Slide</p></div>
  <div class="grid">
    <div class="item"><div class="num">01</div><div><p class="h">Heading here</p><p class="copy">Short line of text for this point.</p></div></div>
    <div class="item"><div class="num">04</div><div><p class="h">Heading here</p><p class="copy">Short line of text for this point.</p></div></div>
    <div class="item"><div class="num">02</div><div><p class="h">Heading here</p><p class="copy">Short line of text for this point.</p></div></div>
    <div class="item"><div class="num">05</div><div><p class="h">Heading here</p><p class="copy">Short line of text for this point.</p></div></div>
    <div class="item"><div class="num">03</div><div><p class="h">Heading here</p><p class="copy">Short line of text for this point.</p></div></div>
    <div class="item"><div class="num">06</div><div><p class="h">Heading here</p><p class="copy">Short line of text for this point.</p></div></div>
  </div>
</section>

<!-- Mission -->
<section class="slide mission col-l r2">
  <div class="topline"></div><div class="accent"><span class="a1"></span><span class="a2"></span><span class="a3"></span><span class="a4"></span></div>
  <div class="brand"><i></i>Dravomell</div>
  <div class="head-block"><p class="eyebrow">What drives us</p><p class="title">Our Mission</p></div>
  <div class="cards">
    <div class="card"><div class="ico"><svg width="12" height="12" viewBox="0 0 12 12"><path d="M2 6l3 3 5-6" fill="none" stroke="currentColor" stroke-width="1.5"/></svg></div><p class="h">Heading 1</p><p class="copy">Clear fixed offers that are easy to plan.</p></div>
    <div class="card"><div class="ico"><svg width="12" height="12" viewBox="0 0 12 12"><circle cx="5" cy="5" r="3.5" fill="none" stroke="currentColor" stroke-width="1.3"/><path d="M7.5 7.5L11 11" stroke="currentColor" stroke-width="1.3"/></svg></div><p class="h">Heading 2</p><p class="copy">Full transparency in every project step.</p></div>
    <div class="card dark"><div class="ico"><svg width="12" height="12" viewBox="0 0 12 12"><path d="M2 3h8M2 6h8M2 9h8" stroke="currentColor" stroke-width="1.3"/></svg></div><p class="h">Heading 3</p><p class="copy">Quality support for peace of mind.</p></div>
  </div>
</section>

<!-- Service -->
<section class="slide service col-r r2">
  <div class="topline"></div><div class="accent"><span class="a1"></span><span class="a2"></span><span class="a3"></span><span class="a4"></span></div>
  <div class="brand"><i></i>Dravomell</div>
  <div class="head-block"><p class="eyebrow">What we offer</p><p class="title">Our Service</p></div>
  <div class="row">
    <div class="cell"><div class="photo" role="img" aria-label="Photo of a laptop workspace"></div><div class="sq"></div><p class="h">Description</p><p class="copy">Short service text here.</p></div>
    <div class="cell"><div class="photo" role="img" aria-label="Photo of a team meeting"></div><div class="sq"></div><p class="h">Description</p><p class="copy">Short service text here.</p></div>
    <div class="cell"><div class="photo" role="img" aria-label="Photo of a desk with a notebook"></div><div class="sq"></div><p class="h">Description</p><p class="copy">Short service text here.</p></div>
  </div>
</section>

<!-- About -->
<section class="slide about col-l r3">
  <div class="topline"></div><div class="accent"><span class="a1"></span><span class="a2"></span><span class="a3"></span><span class="a4"></span></div>
  <div class="brand"><i></i>Dravomell</div>
  <div class="head-block"><p class="eyebrow">Who we are</p><p class="title">About Us</p></div>
  <div class="text">
    <p class="copy">We implement ERP systems and build IT infrastructure for small and medium companies across the region.</p>
    <p class="copy">Our flat-rate offers keep every project simple, transparent and easy to plan.</p>
  </div>
  <div class="photo" role="img" aria-label="Photo of a laptop on an office desk"></div>
</section>

<!-- Work -->
<section class="slide work col-r r3">
  <div class="topline"></div><div class="accent"><span class="a1"></span><span class="a2"></span><span class="a3"></span><span class="a4"></span></div>
  <div class="brand"><i></i>Dravomell</div>
  <div class="head-block"><p class="eyebrow">Results</p><p class="title">Our Work</p></div>
  <div class="stats">
    <div class="box light"><svg width="22" height="22" viewBox="0 0 22 22"><circle cx="8" cy="8" r="3" fill="var(--ink)"/><circle cx="15" cy="8" r="3" fill="var(--ink)"/><path d="M2 18c1-5 11-5 12 0M9 18c1-5 10-5 11 0" fill="none" stroke="var(--ink)" stroke-width="1.6"/></svg></div>
    <div class="box dark">$39,999</div>
    <div class="box dark">$24,900</div>
    <div class="box light"><svg width="22" height="22" viewBox="0 0 22 22"><rect x="3" y="5" width="16" height="12" fill="none" stroke="var(--ink)" stroke-width="1.6"/><path d="M3 9h16" stroke="var(--ink)" stroke-width="1.6"/></svg></div>
  </div>
  <div class="photo" role="img" aria-label="Photo of colleagues working at a computer"></div>
</section>

<!-- Section break -->
<section class="slide section col-l r4">
  <div class="frame"><p class="eyebrow">Part two</p><p class="title">Section Break</p></div>
</section>

<!-- Process -->
<section class="slide process col-r r4">
  <div class="topline"></div><div class="accent"><span class="a1"></span><span class="a2"></span><span class="a3"></span><span class="a4"></span></div>
  <div class="brand"><i></i>Dravomell</div>
  <div class="head-block" style="top:80px"><p class="eyebrow">How we work</p><p class="title">Our Process</p></div>
  <div class="text"><p class="copy">From first talk to live system, each stage has a clear scope, a fixed price and a named contact.</p></div>
  <div class="list">
    <div class="item"><div class="num">01</div><div><p class="h">Team here</p><p class="copy">Short step text.</p></div></div>
    <div class="item"><div class="num">02</div><div><p class="h">Team here</p><p class="copy">Short step text.</p></div></div>
    <div class="item"><div class="num">03</div><div><p class="h">Team here</p><p class="copy">Short step text.</p></div></div>
    <div class="item"><div class="num">04</div><div><p class="h">Team here</p><p class="copy">Short step text.</p></div></div>
  </div>
</section>

<!-- Laptop -->
<section class="slide laptop col-l r5">
  <div class="topline"></div><div class="accent"><span class="a1"></span><span class="a2"></span><span class="a3"></span><span class="a4"></span></div>
  <div class="brand"><i></i>Dravomell</div>
  <div class="head-block"><p class="eyebrow">Show your screen</p><p class="title">Laptop Mockup</p></div>
  <div class="list">
    <div class="item"><div class="num" style="width:14px;height:14px"></div><div><p class="h">Features</p><p class="copy">Short feature text goes here.</p></div></div>
    <div class="item"><div class="num" style="width:14px;height:14px"></div><div><p class="h">Features</p><p class="copy">Short feature text goes here.</p></div></div>
  </div>
  <div class="photo" role="img" aria-label="Laptop with a dashboard screen beside a phone"></div>
</section>

<!-- Chart -->
<section class="slide chart col-r r5">
  <div class="topline"></div><div class="accent"><span class="a1"></span><span class="a2"></span><span class="a3"></span><span class="a4"></span></div>
  <div class="brand"><i></i>Dravomell</div>
  <div class="head-block"><p class="eyebrow">Figures</p><p class="title">Our Chart</p></div>
  <svg class="bars" width="260" height="150" viewBox="0 0 260 150">
    <g fill="var(--ink)">
      <rect x="30" y="6" width="150" height="9"/><rect x="30" y="40" width="200" height="9"/><rect x="30" y="74" width="120" height="9"/><rect x="30" y="108" width="170" height="9"/>
    </g>
    <g fill="var(--soft)">
      <rect x="30" y="17" width="100" height="9"/><rect x="30" y="51" width="140" height="9"/><rect x="30" y="85" width="80" height="9"/><rect x="30" y="119" width="110" height="9"/>
    </g>
    <path d="M30 2v132h225" fill="none" stroke="var(--line)"/>
    <g font-size="6" fill="var(--grey)" font-family="Poppins, sans-serif">
      <text x="0" y="19">Item 1</text><text x="0" y="53">Item 2</text><text x="0" y="87">Item 3</text><text x="0" y="121">Item 4</text>
      <text x="28" y="145">0</text><text x="90" y="145">50</text><text x="150" y="145">100</text><text x="210" y="145">150</text>
    </g>
  </svg>
  <div class="side">
    <p class="h">NAME CHART</p>
    <div class="item"><div class="num" style="width:14px;height:14px"></div><div><p class="h">Series one</p><p class="copy">Short legend text.</p></div></div>
    <div class="item"><div class="num" style="width:14px;height:14px;background:var(--soft)"></div><div><p class="h">Series two</p><p class="copy">Short legend text.</p></div></div>
  </div>
</section>

<!-- Testimonial -->
<section class="slide testi col-l r6">
  <div class="topline"></div><div class="accent"><span class="a1"></span><span class="a2"></span><span class="a3"></span><span class="a4"></span></div>
  <div class="brand"><i></i>Dravomell</div>
  <div class="quotes">
    <div class="q"><div class="avatar" role="img" aria-label="Client portrait"></div><div><p class="h">Client name</p><p class="copy">Clear price and fast, friendly support.</p></div></div>
    <div class="q light"><div class="avatar" role="img" aria-label="Client portrait"></div><div><p class="h">Client name</p><p class="copy">Clear price and fast, friendly support.</p></div></div>
    <div class="q"><div class="avatar" role="img" aria-label="Client portrait"></div><div><p class="h">Client name</p><p class="copy">Clear price and fast, friendly support.</p></div></div>
    <div class="q"><div class="avatar" role="img" aria-label="Client portrait"></div><div><p class="h">Client name</p><p class="copy">Clear price and fast, friendly support.</p></div></div>
  </div>
  <div class="head"><p class="eyebrow">What clients say</p><p class="title">Testimonial<br>Goes Here</p></div>
</section>

<!-- Thank you -->
<section class="slide thanks col-r r6">
  <div class="photo" role="img" aria-label="Photo of hands typing on a laptop"></div>
  <div class="panel">
    <div class="brand" style="position:static;align-self:flex-start;color:var(--white);border-color:var(--white)"><i style="background:var(--white)"></i>Dravomell</div>
    <p>THANK YOU FOR<br>WATCHING!</p>
  </div>
</section>

</body>
</html>
```